Website plus logo for a finance business (in Wix)

We need a revamp of our website and our logo - visit www.halvernbridging.com for the current site.

We are a relatively new finance firm, providing short term (bridging) loans to property developers and other businesses in the UK.

Most of the information will go on the homepage. The other 3 or 4 pages are relatively basic. If you felt it was appropriate, the information on page 2 (case studies) could be incorporated on page 1.

The current website isn't too bad and gives you an idea of the information we would like covering on the website and in what order.

The logo should be clean, simple and modern, probably branded around a rocket. The current logo is a good starting point. The word rocket should be the focal point though.

The main header colour scheme should be similar to the current website (deep purples) but we would consider dark blues or reds. An example of a palette of colours we really like is attached.

The style should be modern and clean. Lots of whites and background space but with an underlying warmth, suggesting trust and reliability.

Examples of good brands and websites that we like in our sector are www.brindlefunds.com, www.quarlowlending.co.uk and www.veltrope.co.uk - we particularly like Veltrope.

Important note - as part of the service, the website designer must be able to create the website in Wix once the design is approved. Our current website is through Wix and we want to keep it that way.

Therefore, once the design is approved, as part of the finalisation process, the designer will need to create the website in our existing Wix account.

This will also involve creating a mobile friendly version of the site (which is more or less automatic in Wix anyway). None of this should be difficult as Wix is very easy to use.

Thanks for your interest!

Kind regards

HalvernBridging

Target Market(s)

Small to medium property developers and businesses in the North West of the UK

Industry/Entity Type

Finance

Contact Information for Business Card

One side just feature the logo against a strong background colour.
The other side should have a nice clean look about it, with the details of our sales director, Tessa Marwick.
tessa@halvernbridging.com
0161 555 0193
07700 900418

Logo Text

Halvern Bridging

Coding

Coded - Design and coding required

Number of Pages Required

4 page

Font styles to use
Sans Serif

Colors
6b449b
0456a4

Requirements
Must have
• Clean looking home page, modelled on the examples that we've given.
• The start of the home page must make it clear what we do - this could be achieved by rotating banners.
• Must be produced in Wix once the design is approved.
• Should follow example colour palette given.
Nice to have
• Parallax pictures
Should not have
• Old fashioned or traditional styling - we do not want to look like an accountant or law firm's website

```html
<!DOCTYPE html>
<html lang="en">
<head>
<meta charset="utf-8">
<title>Halvern Bridging – Website Screens</title>
<link rel="stylesheet" href="https://fonts.googleapis.com/css2?family=Montserrat:wght@300;400;600;700;800&family=Open+Sans:wght@400;600&display=swap">
<style>
  :root{
    --page:#ffffff;
    --navy:#211d38;
    --navy-deep:#1b1830;
    --ink:#24213a;
    --pink:#e6177f;
    --rose:#d06f9f;
    --rose-deep:#b9588a;
    --cream:#fde9dd;
    --charcoal:#2c2c2e;
    --field:#9a9a9a;
    --white:#ffffff;
    --link:#6fb8e8;
  }
  *{box-sizing:border-box;margin:0;padding:0}
  html,body{width:1200px;height:1200px;overflow:hidden;background:var(--page)}
  body{position:relative;font-family:"Montserrat",sans-serif;color:var(--ink)}

  .screen{position:absolute;top:402px;height:300px;overflow:hidden}

  /* Contact screen */
  .screen--contact{left:86px;width:256px;background:var(--cream)}
  .contact__stage{position:absolute;left:0;top:29px;width:256px;height:243px;background:var(--charcoal)}
  .contact__backdrop{position:absolute;left:0;top:22px;width:256px;height:200px;background:linear-gradient(90deg,#3a3a3c,#2f2f31 60%,#343436)}
  .contact__brand{position:absolute;left:59px;top:8px;font-size:6.5px;font-weight:700;letter-spacing:2px;color:#555}
  .chat-card{position:absolute;left:99px;top:30px;width:170px;height:188px;background:var(--white);border:1px solid #bbb}
  .chat-card__frame{position:absolute;inset:3px;border:1px solid #555}
  .chat-card__avatar{position:absolute;left:111px;top:12px;width:48px;height:48px;border-radius:50%;background:radial-gradient(circle at 50% 40%,#c9a27f,#7a5a44)}
  .chat-card__title{position:absolute;left:57px;top:76px;font-size:13px;font-weight:800;letter-spacing:.5px;color:#111}
  .chat-card__lead{position:absolute;left:57px;top:92px;font-family:"Open Sans",sans-serif;font-size:4.8px;color:#333;white-space:nowrap}
  .field{position:absolute;left:57px;width:84px;height:11px;border:1px solid var(--field);font-family:"Open Sans",sans-serif;font-size:5px;color:#888;padding:2px 2px}
  .field--message{left:144px;width:30px;height:47px}
  .contact__foot{position:absolute;left:115px;top:234px;font-family:"Open Sans",sans-serif;font-size:4.5px;color:#4a4a4a;white-space:nowrap}

  /* Home screen */
  .screen--home{left:362px;width:481px;background:var(--navy)}
  .nav{position:absolute;left:0;top:0;width:100%;height:22px;display:flex;align-items:center}
  .nav__brand{position:absolute;left:60px;font-size:6.5px;font-weight:700;letter-spacing:2px;color:var(--white)}
  .nav__links{position:absolute;left:290px;display:flex;gap:11px;font-family:"Open Sans",sans-serif;font-size:5px;color:var(--white)}
  .nav__links .is-active{color:var(--link)}
  .hero{position:absolute;left:0;top:22px;width:481px;height:238px;background:linear-gradient(100deg,#5d6470 0%,#3f4656 35%,#2c3345 55%,#6a7280 80%,#8e95a0 100%)}
  .hero__copy{position:absolute;left:0;top:92px;width:100%;text-align:center}
  .hero__kicker{font-size:9px;font-weight:400;color:var(--pink);letter-spacing:.3px}
  .hero__title{font-size:20px;font-weight:600;color:var(--pink);letter-spacing:1.6px;line-height:1.1}
  .hero__points{font-family:"Open Sans",sans-serif;font-size:6.2px;font-weight:600;color:var(--white);line-height:1.35;margin-top:2px}
  .section-head{position:absolute;left:0;top:284px;width:100%;text-align:center;font-size:24px;font-weight:700;color:var(--white)}

  /* About screen */
  .screen--about{left:862px;width:254px;background:var(--navy)}
  .about__thumb{position:absolute;left:0;top:0;width:66px;height:37px;background:linear-gradient(135deg,#4a4f5e,#2d3140)}
  .about__thumb-rule{position:absolute;left:0;top:17px;width:38px;height:1px;background:var(--link)}
  .about__panel{position:absolute;left:0;top:58px;width:254px;height:229px;background:linear-gradient(100deg,var(--rose) 0%,#cf79a5 55%,var(--rose-deep) 100%)}
  .about__title{position:absolute;left:-62px;top:66px;font-size:30px;font-weight:800;color:var(--white);white-space:nowrap;letter-spacing:.5px}
  .about__text{position:absolute;left:-4px;top:104px;font-family:"Open Sans",sans-serif;font-size:5.6px;color:var(--white);line-height:1.55;white-space:nowrap}
  .about__button{position:absolute;left:-10px;top:131px;width:63px;height:15px;background:var(--charcoal);color:var(--white);font-family:"Open Sans",sans-serif;font-size:5.6px;padding:4px 0 0 10px}
  .about__foot{position:absolute;left:0;top:287px;width:254px;height:13px;background:var(--navy-deep)}

  .caption{position:absolute;left:0;top:918px;width:100%;text-align:center;font-size:38px;font-weight:400;letter-spacing:4px;color:var(--ink)}
</style>
</head>
<body>

<section class="screen screen--contact" aria-label="Contact page">
  <div class="contact__stage">
    <div class="contact__brand">HALVERN BRIDGING</div>
    <div class="contact__backdrop" role="img" aria-label="Dimmed office photograph behind the contact popup"></div>
    <div class="chat-card">
      <div class="chat-card__frame"></div>
      <div class="chat-card__avatar" role="img" aria-label="Portrait of the client manager"></div>
      <div class="chat-card__title">LET'S CHAT</div>
      <div class="chat-card__lead">Tessa is our Client Manager and will be</div>
      <div class="field" style="top:107px">Email *</div>
      <div class="field" style="top:121px">Name *</div>
      <div class="field" style="top:135px">Subject</div>
      <div class="field field--message" style="top:107px">Mes</div>
    </div>
    <div class="contact__foot">Site built with a website builder</div>
  </div>
</section>

<section class="screen screen--home" aria-label="Home page">
  <nav class="nav">
    <div class="nav__brand">HALVERN BRIDGING</div>
    <div class="nav__links">
      <span class="is-active">Home</span><span>About</span><span>Services</span><span>Clients</span><span>Contact</span>
    </div>
  </nav>
  <div class="hero" role="img" aria-label="Photograph of a smiling team seated around a meeting table">
    <div class="hero__copy">
      <div class="hero__kicker">BRIDGE FUNDING</div>
      <div class="hero__title">THE MODERN WAY</div>
      <div class="hero__points">NO FIXED LENDING CRITERIA<br>LTVs UP TO 85%</div>
    </div>
  </div>
  <div class="section-head">About Us</div>
</section>

<section class="screen screen--about" aria-label="About page">
  <div class="about__thumb" role="img" aria-label="Small photograph of a professional"></div>
  <div class="about__thumb-rule"></div>
  <div class="about__panel" role="img" aria-label="Pink-toned photograph of businessmen in an office"></div>
  <div class="about__title">TALK TO US</div>
  <div class="about__text">riteria, it's best to get in touch. Tessa,<br>&nbsp;&nbsp;first point of contact.</div>
  <div class="about__button">ad More &gt;&gt;</div>
  <div class="about__foot"></div>
</section>

<h1 class="caption">HALVERN BRIDGING</h1>

</body>
</html>
```